Business Card for Business consulting practice

Need a design for a consultant business card. Simple and elegant.
I need the following information on the card:
Logo: (see uploaded file)
Company name: Calmora Advisory Group
Name: Dana Weltrup
Title: Managing Director - Aerospace and Defence
Phone #: 514-268-3917
e-mail: dana.weltrup@calmora-example.com
Website: www.calmora-example.com
Tagline: Proposals Management and Capture support for complex procurements

```html
<!DOCTYPE html>
<html lang="en">
<head>
<meta charset="utf-8">
<title>Calmora Advisory Group – Business Card</title>
<link rel="stylesheet" href="https://fonts.googleapis.com/css2?family=Cinzel:wght@600;700&family=Montserrat:wght@400;500&family=Josefin+Sans:wght@400&display=swap">
<style>
  :root {
    --bg: #c9c9c9;
    --card-white: #f7f7f7;
    --band-blue: #4a89b5;
    --navy: #1f2e42;
    --ink: #1f2e42;
    --accent: #4a89b5;
    --on-navy: #ffffff;
  }
  * { margin: 0; padding: 0; box-sizing: border-box; }
  html, body { width: 1200px; height: 857px; overflow: hidden; }
  body { background: var(--bg); position: relative; }

  .card {
    position: absolute;
    width: 540px;
    height: 309px;
    box-shadow: 0 14px 30px rgba(0,0,0,0.28);
    overflow: hidden;
  }
  .card-front { left: 60px; top: 150px; }
  .card-back  { left: 600px; top: 400px; }
  .card-art { position: absolute; inset: 0; width: 100%; height: 100%; }

  .company {
    position: absolute;
    left: 36px;
    top: 98px;
    font-family: "Cinzel", serif;
    font-weight: 700;
    font-size: 25px;
    line-height: 1.15;
    letter-spacing: 1px;
    color: var(--ink);
  }
  .company-rule {
    position: absolute;
    left: 36px;
    top: 166px;
    width: 280px;
    height: 1.5px;
    background: var(--accent);
  }
  .tagline {
    position: absolute;
    left: 36px;
    top: 180px;
    width: 270px;
    font-family: "Montserrat", sans-serif;
    font-weight: 500;
    font-size: 13px;
    line-height: 1.35;
    color: var(--accent);
  }
  .website {
    position: absolute;
    right: 18px;
    bottom: 24px;
    font-family: "Montserrat", sans-serif;
    font-size: 12px;
    white-space: nowrap;
    color: var(--on-navy);
    letter-spacing: 0.2px;
  }

  .person-name {
    position: absolute;
    left: 36px;
    top: 58px;
    font-family: "Cinzel", serif;
    font-weight: 700;
    font-size: 17px;
    letter-spacing: 0.5px;
    color: var(--ink);
  }
  .person-title {
    position: absolute;
    left: 36px;
    top: 82px;
    font-family: "Josefin Sans", sans-serif;
    font-size: 14px;
    line-height: 1.25;
    color: var(--accent);
  }
  .contact-list {
    position: absolute;
    left: 36px;
    top: 160px;
    list-style: none;
    font-family: "Josefin Sans", sans-serif;
    font-size: 14px;
    color: var(--ink);
  }
  .contact-item { display: flex; align-items: center; gap: 9px; height: 24px; }
  .contact-icon { width: 18px; height: 18px; flex: none; }
</style>
</head>
<body>

  <section class="card card-front" aria-label="Card front">
    <svg class="card-art" viewBox="0 0 540 309" preserveAspectRatio="none" aria-hidden="true">
      <defs>
        <radialGradient id="navyGlowFront" cx="0.6" cy="0.35" r="0.6">
          <stop offset="0" stop-color="#2e3f58"/>
          <stop offset="1" stop-color="#1f2e42"/>
        </radialGradient>
      </defs>
      <rect width="540" height="309" fill="var(--card-white)"/>
      <polygon points="185,0 540,0 540,309 290,309 365,135 345,105" fill="var(--band-blue)"/>
      <polygon points="240,0 540,0 540,309 340,309 420,135 400,105" fill="url(#navyGlowFront)"/>
    </svg>
    <div class="company">Calmora<br>Advisory Group</div>
    <div class="company-rule"></div>
    <p class="tagline">Proposals Management and Capture support for complex procurements</p>
    <p class="website">www.calmora-example.com</p>
  </section>

  <section class="card card-back" aria-label="Card back">
    <svg class="card-art" viewBox="0 0 540 309" preserveAspectRatio="none" aria-hidden="true">
      <defs>
        <radialGradient id="navyGlowBack" cx="0.6" cy="0.45" r="0.6">
          <stop offset="0" stop-color="#2e3f58"/>
          <stop offset="1" stop-color="#1f2e42"/>
        </radialGradient>
      </defs>
      <rect width="540" height="309" fill="var(--card-white)"/>
      <polygon points="230,0 540,0 540,309 230,309 345,170 325,125" fill="var(--band-blue)"/>
      <polygon points="290,0 540,0 540,309 290,309 395,175 378,128" fill="url(#navyGlowBack)"/>
      <circle class="mark-circle" cx="462" cy="165" r="34" fill="none" stroke="var(--band-blue)" stroke-width="6"/>
    </svg>
    <h2 class="person-name">Dana Weltrup</h2>
    <p class="person-title">Managing Director<br>Aerospace and Defence</p>
    <ul class="contact-list">
      <li class="contact-item">
        <svg class="contact-icon" viewBox="0 0 18 18" aria-hidden="true">
          <circle cx="9" cy="9" r="9" fill="var(--band-blue)"/>
          <path d="M6 4.8c.4-.3.9-.2 1.1.2l.8 1.5c.2.4.1.8-.2 1.1l-.5.4c.5 1.1 1.3 1.9 2.4 2.4l.4-.5c.3-.3.7-.4 1.1-.2l1.5.8c.4.2.5.7.2 1.1l-.6.8c-.4.5-1.1.6-1.700.4C8 11.9 6.1 10 5.2 7.6c-.2-.6-.1-1.3.4-1.7z" fill="#fff"/>
        </svg>
        <span>514-268-3917</span>
      </li>
      <li class="contact-item">
        <svg class="contact-icon" viewBox="0 0 18 18" aria-hidden="true">
          <circle cx="9" cy="9" r="9" fill="var(--band-blue)"/>
          <rect x="4.5" y="6" width="9" height="6.5" rx="0.8" fill="none" stroke="#fff" stroke-width="1.1"/>
          <path d="M4.8 6.4 9 9.6l4.2-3.2" fill="none" stroke="#fff" stroke-width="1.1"/>
        </svg>
        <span>dana.weltrup@calmora-example.com</span>
      </li>
    </ul>
  </section>

</body>
</html>
```